Roofing Company Sales Rep Business Card

Business card for sales rep to canvass and hand out to property owners/managers for free roof inspections and roof replacements.

```html
<!DOCTYPE html>
<html lang="en">
<head>
<meta charset="UTF-8">
<title>Summit Crest Roofing – Business Card</title>
<link href="https://fonts.googleapis.com/css2?family=Montserrat:wght@400;500;700;800&display=swap" rel="stylesheet">
<style>
  :root {
    --page-bg: #b9b9b9;
    --card-white: #ffffff;
    --card-black: #1c1c1c;
    --brand-red: #e3242b;
    --ink: #1e1e1e;
    --silver: #d4d4d4;
  }
  * { margin: 0; padding: 0; box-sizing: border-box; }
  html, body { width: 1200px; height: 900px; overflow: hidden; }
  body {
    background: var(--page-bg);
    font-family: "Montserrat", sans-serif;
    display: flex;
    flex-direction: column;
    align-items: center;
    justify-content: center;
    gap: 50px;
  }
  .card {
    width: 630px;
    height: 360px;
    border-radius: 18px;
    position: relative;
    overflow: hidden;
    box-shadow: 0 10px 26px rgba(0,0,0,0.18);
  }
  .card-front {
    background: var(--card-white);
    display: flex;
    align-items: center;
  }
  .front-brand {
    width: 300px;
    display: flex;
    align-items: center;
    justify-content: center;
    gap: 12px;
  }
  .brand-mark {
    width: 16px; height: 16px;
    background: var(--brand-red);
    flex: none;
  }
  .brand-name {
    font-weight: 800;
    font-size: 25px;
    line-height: 1.1;
    color: var(--ink);
    text-transform: uppercase;
    letter-spacing: 0.5px;
  }
  .divider {
    width: 2px;
    height: 170px;
    background: var(--brand-red);
  }
  .front-details {
    padding-left: 34px;
    color: var(--ink);
  }
  .rep-name {
    font-weight: 700;
    font-size: 27px;
    color: var(--brand-red);
    line-height: 1.1;
  }
  .rep-title {
    font-size: 15px;
    margin-bottom: 20px;
  }
  .contact-list { list-style: none; font-size: 14px; line-height: 1.7; }
  .contact-list li { display: flex; align-items: center; gap: 9px; }
  .contact-list svg { width: 13px; height: 13px; flex: none; fill: var(--brand-red); }
  .address { font-size: 14px; line-height: 1.45; margin-top: 12px; }

  .card-back {
    background: var(--card-black);
    display: flex;
    align-items: center;
    justify-content: center;
    gap: 18px;
  }
  .card-back .brand-mark { width: 24px; height: 24px; background: var(--silver); }
  .card-back .brand-name { color: var(--silver); font-size: 44px; }
</style>
</head>
<body>
  <section class="card card-front">
    <div class="front-brand">
      <span class="brand-mark"></span>
      <span class="brand-name">Summit Crest<br>Roofing</span>
    </div>
    <div class="divider"></div>
    <div class="front-details">
      <h1 class="rep-name">Daniel Brooks</h1>
      <p class="rep-title">Owner</p>
      <ul class="contact-list">
        <li><svg viewBox="0 0 24 24"><path d="M6.6 10.8a15.1 15.1 0 0 0 6.6 6.6l2.2-2.2a1 1 0 0 1 1-.25 11.4 11.4 0 0 0 3.6.57 1 1 0 0 1 1 1V20a1 1 0 0 1-1 1A17 17 0 0 1 3 4a1 1 0 0 1 1-1h3.5a1 1 0 0 1 1 1c0 1.25.2 2.45.57 3.6a1 1 0 0 1-.25 1z"/></svg>215-555-0147</li>
        <li><svg viewBox="0 0 24 24"><path d="M2 5h20v14H2zm2 2v.5l8 5 8-5V7l-8 5z"/></svg>hello@summitcrestroofing.com</li>
        <li><svg viewBox="0 0 24 24"><circle cx="12" cy="12" r="10"/></svg>www.summitcrestroofing.com</li>
      </ul>
      <p class="address">48 Harbor Lane, Suite 20<br>Ridgefield, PA 18000</p>
    </div>
  </section>

  <section class="card card-back">
    <span class="brand-mark"></span>
    <span class="brand-name">Summit Crest Roofing</span>
  </section>
</body>
</html>
```